Pelmora needs stationery design

We need desings for presentation cards and letter head for our company. It would be better that the letterhead uses our logo with white background and the presentation card the logo with the black background for the back of the card and the text (name, phone
Updates

Necesitas un par de días antes de escoger al ganador

Colors
0455a3
ec1f27
000000

Requirements
Must have
• Use company logo and colors

```html
<!DOCTYPE html>
<html lang="en">
<head>
<meta charset="utf-8">
<title>Pelmora Letterhead</title>
<link rel="stylesheet" href="https://fonts.googleapis.com/css2?family=Quicksand:wght@400;500;600;700&family=Poppins:wght@500&display=swap">
<style>
  :root {
    --brand-blue: #0455a3;
    --brand-red: #ec1f27;
    --ink: #000000;
    --text: #2b2b2b;
    --muted: #555555;
    --backdrop: #0c4d92;
    --paper: #fbfbfb;
    --signature-tone: #d6d6d6;
  }
  * { box-sizing: border-box; margin: 0; padding: 0; }
  html, body {
    width: 1200px; height: 1187px; overflow: hidden;
    background: var(--backdrop);
  }
  body { position: relative; font-family: "Quicksand", sans-serif; color: var(--text); }

  .letterhead {
    position: absolute; left: 175px; top: 48px;
    width: 849px; height: 1090px;
    background: var(--paper);
    overflow: hidden;
  }
  .letterhead > * { position: absolute; }

  .brand {
    left: 47px; top: 88px;
    display: flex; align-items: center; gap: 10px;
  }
  .brand-mark { width: 14px; height: 14px; background: var(--brand-red); }
  .brand-name {
    font-family: "Quicksand", sans-serif; font-weight: 600;
    font-size: 44px; letter-spacing: 2px; color: var(--ink); line-height: 1;
  }

  .contact-block {
    top: 94px; height: 42px;
    border-left: 2px solid var(--brand-red);
    padding-left: 15px;
    font-family: "Poppins", sans-serif; font-weight: 500;
    font-size: 13px; line-height: 21px; color: var(--muted);
  }
  .contact-address { left: 402px; }
  .contact-address .company { color: var(--brand-blue); }
  .contact-direct { left: 627px; }
  .contact-line { display: flex; align-items: center; gap: 9px; }
  .contact-line svg { width: 12px; height: 12px; fill: none; stroke: var(--brand-blue); stroke-width: 2; }
  .contact-line .icon-phone { fill: var(--brand-blue); stroke: none; }

  .recipient { left: 48px; top: 292px; font-size: 17px; line-height: 29px; }
  .recipient-name { color: var(--brand-blue); font-weight: 500; }
  .recipient-title { color: var(--text); font-weight: 500; }
  .recipient-address { margin-top: 8px; line-height: 30px; font-weight: 500; }

  .letter-date {
    right: 49px; top: 292px; font-size: 17px; line-height: 29px;
    font-weight: 600; color: var(--text);
  }

  .letter-body {
    left: 48px; top: 440px; width: 752px;
    font-size: 16.4px; line-height: 29px; font-weight: 500;
    text-align: justify; color: var(--text);
  }
  .letter-body p + p { margin-top: 29px; }

  .sign-off { left: 48px; top: 808px; font-size: 13px; font-weight: 500; }
  .signature {
    left: 48px; top: 834px; width: 120px; height: 44px;
    background: linear-gradient(90deg, var(--signature-tone), #ececec);
    border-radius: 4px;
  }
  .signer { left: 48px; top: 890px; font-size: 15px; font-weight: 500; color: var(--muted); }

  .footer-band { left: 0; bottom: 0; width: 849px; height: 48px; }
  .footer-url {
    left: 0; width: 849px; bottom: 16px; text-align: center;
    font-family: "Poppins", sans-serif; font-weight: 500;
    font-size: 19px; letter-spacing: 3px; color: #ffffff;
  }
</style>
</head>
<body>
  <main class="letterhead">
    <div class="brand">
      <span class="brand-name">PELMORA</span>
      <span class="brand-mark"></span>
    </div>

    <div class="contact-block contact-address">
      <div><span class="company">Pelmora</span> - 418 W 17th St. Ste</div>
      <div>204B Halden, VA 23611</div>
    </div>

    <div class="contact-block contact-direct">
      <div class="contact-line">
        <svg viewBox="0 0 24 24"><path class="icon-phone" d="M6.6 10.8a15 15 0 0 0 6.6 6.6l2.2-2.2a1 1 0 0 1 1-.25 11.4 11.4 0 0 0 3.6.57 1 1 0 0 1 1 1V20a1 1 0 0 1-1 1A17 17 0 0 1 3 4a1 1 0 0 1 1-1h3.5a1 1 0 0 1 1 1c0 1.25.2 2.45.57 3.57a1 1 0 0 1-.25 1z"/></svg>
        <span>+809 555 0142</span>
      </div>
      <div class="contact-line">
        <svg viewBox="0 0 24 24"><rect x="3" y="5" width="18" height="14" rx="1"/><path d="M3 6l9 7 9-7"/></svg>
        <span>info@pelmora.com</span>
      </div>
    </div>

    <div class="recipient">
      <div class="recipient-name">Étienne Marsolle</div>
      <div class="recipient-title">Corvane Technical Architect/Director</div>
      <div class="recipient-address">
        <div>12 Allée Verdane</div>
        <div>Corvelle, 31000 Lorvaux</div>
      </div>
    </div>

    <div class="letter-date">Date: 12/11/2018</div>

    <div class="letter-body">
      <p>Lorem ipsum dolor sit amet, consectetuer adipiscing elit, sed diam nonummy nibh euismod tincidunt ut laoreet dolore magna aliquam erat volutpat. Ut wisi enim ad minim veniam, quis nostrud exerci tation ullamcorper suscipit lobortis nisl ut aliquip ex ea commodo consequat. Lorem ipsum dolor sit amet, cons ectetuer adipiscing elit, sed diam nonummy nibh euismod tincidunt ut laoreet dolore magna aliquam erat volutpat. Ut wisi enim ad minim veniam,</p>
      <p>quis nostrud exerci tation ullamcorper suscipit lobortis nisl ut aliquip ex ea commodo consequat. Lorem ipsum dolor sit amet, consectetuer adipiscing elit, sed diam nonummy nibh euismod tincidunt ut laoreet dolore magna aliquam erat volutpat. Ut wisi enim ad minim veniam,</p>
      <p>consequat. Duis autem vel eum iriure dolor in hendrerit in vulputate velit esse molestie consequat, vel illum dolore eu feugiat nulla facilisis at vero eros et accumsan .</p>
    </div>

    <div class="sign-off">sincerely</div>
    <div class="signature" role="img" aria-label="Handwritten signature of the sender"></div>
    <div class="signer">Daniel Hartwell</div>

    <svg class="footer-band" viewBox="0 0 849 48" preserveAspectRatio="none">
      <rect x="0" y="12" width="290" height="3" fill="var(--brand-red)"/>
      <rect x="559" y="12" width="290" height="3" fill="var(--brand-red)"/>
      <path d="M0 24 H270 C284 24 284 6 300 6 H549 C565 6 565 24 579 24 H849 V48 H0 Z" fill="var(--brand-blue)"/>
    </svg>
    <div class="footer-url">www.pelmora.com</div>
  </main>
</body>
</html>
```